Peter Lanford Studios Business Card

Looking for a clear, modern, elegant, sharp business card that conveys a professional yet edgy image to my business as a wedding, portrait, and travel photographer. Would like something that looks vintage yet modern. Need a new business card to grow my business. We are growing the business for Wedding and Event Photography as well as fine art Photography. (Mostly Landscapes)
Updates

I’m looking through designs now but I have a new logo that i want using please.

New logo uploaded please redesign using that

PLEASE ALL DESIGNERS LOOK IN BRIEF FOR NEW LOGO

Target Market(s)

Brides, Grooms, Families with Kids, People looking for Fine Art Photography Artwork

Industry/Entity Type

Photographer

Contact Information for Business Card

Unsure

Font styles to use
Serif

Colors

Designer to choose colors to be used in the design.

Requirements
Must have
• My Website:
• http://lanfordgallery.snapfolio.example
• Phone:
• 555-418-2061
• Email:
• petelanfordgallery@mailbox.example
Nice to have
• Would like a sort of shine on the printing finish.
• I like black I think it looks good on a business card.
• Can try working with my logo (png that I've attached)

```html
<!DOCTYPE html>
<html lang="en">
<head>
<meta charset="utf-8">
<title>Peter Lanford Studios – Business Card</title>
<link rel="stylesheet" href="https://fonts.googleapis.com/css2?family=Lato:wght@300;400;700&family=Montserrat:wght@300;400&display=swap">
<style>
  :root {
    --backdrop: #e6d9c4;
    --card-black: #0e0e0e;
    --ink-white: #f4f4f4;
    --ink-soft: #e2e2e2;
    --card-shadow: rgba(40, 25, 10, 0.45);
  }
  * { margin: 0; padding: 0; box-sizing: border-box; }
  html, body {
    width: 1064px;
    height: 1200px;
    overflow: hidden;
    background: var(--backdrop);
  }
  .canvas {
    position: relative;
    width: 1064px;
    height: 1200px;
  }
  .card {
    position: absolute;
    left: 197px;
    width: 670px;
    height: 416px;
    background: var(--card-black);
    box-shadow: 4px 6px 10px var(--card-shadow);
    color: var(--ink-white);
    text-align: center;
  }
  .card--back { top: 160px; }
  .card--front { top: 624px; }

  .brand-mark {
    position: absolute;
    left: 50%;
    transform: translateX(-50%);
  }
  .card--back .brand-mark { top: 77px; width: 80px; height: 80px; }
  .card--front .brand-mark { top: 106px; width: 76px; height: 76px; }

  .brand-name {
    position: absolute;
    left: 0;
    right: 0;
    font-family: "Montserrat", "Lato", sans-serif;
    font-weight: 300;
    letter-spacing: 0.01em;
    line-height: 1;
    white-space: nowrap;
  }
  .card--back .brand-name { top: 185px; font-size: 37px; }
  .card--front .brand-name { top: 236px; font-size: 41px; }

  .brand-tagline {
    position: absolute;
    left: 0;
    right: 0;
    font-family: "Montserrat", "Lato", sans-serif;
    font-weight: 400;
    text-transform: uppercase;
    letter-spacing: 0.34em;
    line-height: 1;
    padding-left: 0.34em;
  }
  .card--back .brand-tagline { top: 233px; font-size: 15px; }
  .card--front .brand-tagline { top: 290px; font-size: 17px; }

  .contact {
    position: absolute;
    left: 0;
    right: 0;
    top: 330px;
    font-family: "Lato", sans-serif;
    font-weight: 400;
    font-size: 16.5px;
    line-height: 28px;
    color: var(--ink-soft);
  }
  .contact__label { font-weight: 700; color: var(--ink-white); }
  .contact__divider { margin: 0 6px; }
</style>
</head>
<body>
<main class="canvas">

  <section class="card card--back" aria-label="Business card, contact side">
    <svg class="brand-mark" viewBox="0 0 80 80" aria-hidden="true">
      <rect x="1" y="1" width="78" height="78" fill="none" stroke="var(--ink-white)" stroke-width="2"/>
    </svg>
    <h1 class="brand-name">PETER LANFORD</h1>
    <p class="brand-tagline">Studios</p>
    <div class="contact">
      <p>
        <span class="contact__label">P:</span> 555-418-2061
        <span class="contact__divider">|</span>
        <span class="contact__label">E:</span> petelanfordgallery@mailbox.example
      </p>
      <p><span class="contact__label">W:</span> www.lanfordgallery.snapfolio.example</p>
    </div>
  </section>

  <section class="card card--front" aria-label="Business card, brand side">
    <svg class="brand-mark" viewBox="0 0 76 76" aria-hidden="true">
      <rect x="1" y="1" width="74" height="74" fill="none" stroke="var(--ink-white)" stroke-width="2"/>
    </svg>
    <h2 class="brand-name">PETER LANFORD</h2>
    <p class="brand-tagline">Studios</p>
  </section>

</main>
</body>
</html>
```